hotel's Website

Hotels website redesign for reference pictures, logo etc see http://restwellharbourside.co.uk/

1. 2-3 Special offers on the main page.
2. Booking calender
3. Location Map
4. Picture gallery.
5. Journeyrater reviews.
6. short description
7. Social Media sharing.
8 Phone number and address.

Industry/Entity Type

Hotel

Requirements
Must have
• 1. 2-3 Special offers on the main page.
2. Booking calender
3. Location Map
4. Picture gallery.
5. Journeyrater reviews.
6. short description
7. Social Media sharing.

```html
<!DOCTYPE html>
<html lang="en">
<head>
<meta charset="utf-8">
<title>Restwell Inn London - Victoria</title>
<link href="https://fonts.googleapis.com/css2?family=Arimo:wght@400;700&display=swap" rel="stylesheet">
<style>
:root{
  --page:#313943;
  --nav:#3a424c;
  --band:#3b444f;
  --panel:#363e48;
  --line:#4a535e;
  --text:#e6e9ec;
  --muted:#a9b0b8;
  --soft:#c9ced4;
  --link:#3f9be0;
  --button:#2f86d6;
  --field:#f4f4f4;
  --star:#f1a623;
  --star-off:#8a9098;
}
*{box-sizing:border-box;margin:0;padding:0}
html,body{width:1200px;height:1090px;overflow:hidden;background:var(--page)}
body{font-family:Arimo,Arial,sans-serif;color:var(--text)}
.canvas{position:relative;width:1200px;height:1090px;overflow:hidden;background:var(--page)}
.abs{position:absolute}
a{color:inherit;text-decoration:none}

.top-nav{left:0;top:0;width:1200px;height:21px;background:var(--nav);border-bottom:1px solid #2a3038}
.top-nav a{position:absolute;top:6px;font-size:7.5px;letter-spacing:.3px;color:var(--muted)}
.top-nav a.current{color:#fff}

.brand-mark{left:250px;top:34px;width:36px;height:36px;background:#1e63a8}
.brand-name{left:238px;top:73px;font-size:6px;letter-spacing:1px;color:var(--muted)}
.brand-name-main{left:292px;top:45px;font-size:9px;color:var(--text)}
.brand-divider{left:304px;top:33px;width:1px;height:40px;background:#6c747d}
.brand-location{left:313px;top:48px;font-size:11.5px;color:#fff}
.contact{right:258px;top:45px;text-align:right;font-size:6.8px;line-height:10px;color:var(--soft)}

.hero{left:0;top:95px;width:1200px;height:365px;background:linear-gradient(90deg,#6d5a45 0%,#b0a184 30%,#c8bb98 48%,#9d8f76 62%,#3a2c24 82%,#7f6a3c 100%)}

.reservation{left:237px;top:398px;width:706px;height:82px;background:var(--panel);border-radius:4px 4px 0 0;box-shadow:0 -2px 8px rgba(0,0,0,.35)}
.reservation h2{position:absolute;left:20px;top:33px;font-size:16px;font-weight:400;color:#fff}
.res-label{position:absolute;top:17px;font-size:7.5px;color:var(--soft)}
.res-select{position:absolute;left:228px;top:35px;width:125px;height:17px;background:#444c56;border:1px solid #59626c;font-size:6px;color:var(--soft);padding:4px 5px}
.res-select .caret{position:absolute;right:0;top:0;width:16px;height:15px;border-left:1px solid #59626c}
.res-select .caret:after{content:"";position:absolute;left:4px;top:6px;border:4px solid transparent;border-top:4px solid #dde;border-bottom:0}
.res-date{position:absolute;top:35px;width:74px;height:17px;background:var(--field);border:1px solid #c9c9c9;font-size:6.8px;color:#333;padding:4px 5px}
.res-date svg{position:absolute;right:3px;top:2px}
.res-book{position:absolute;left:562px;top:35px;width:57px;height:17px;background:linear-gradient(#4a9ce4,var(--button));border-radius:2px;font-size:7.5px;color:#fff;text-align:center;line-height:17px}
.res-sep{position:absolute;left:632px;top:33px;width:1px;height:20px;background:#59626c}
.res-option{position:absolute;left:647px;top:39px;font-size:7.5px;color:var(--link)}

.section-title{font-size:13px;font-weight:400;color:#fff;padding-bottom:8px;border-bottom:1px solid var(--line)}
.offers{left:257px;top:494px;width:178px}
.offer{position:relative;height:72px}
.offer .thumb{position:absolute;left:0;top:0;width:65px;height:55px;background:linear-gradient(135deg,#2b5d8c,#7aa6c8 45%,#b8c4cf 60%,#3d4f63)}
.offer .body{position:absolute;left:74px;top:0;width:106px;font-size:6.4px;line-height:10px;color:var(--soft)}
.offer h3{font-size:7.8px;color:#fff;margin-bottom:1px}
.offer .more{color:var(--link)}
.offers-list{margin-top:22px}
.offers-all{display:block;margin-top:-2px;padding-top:6px;font-size:9px;color:var(--link);border-top:1px solid var(--line);padding-bottom:6px;border-bottom:1px solid var(--line)}

.welcome{left:465px;top:494px;width:455px}
.welcome p{margin-top:12px;font-size:6.4px;line-height:10px;color:var(--soft)}
.welcome p:first-of-type{margin-top:20px}
.gallery{left:465px;top:636px;width:455px}
.gallery .view-all{position:absolute;right:0;top:4px;font-size:9px;color:var(--link)}
.gallery-row{display:flex;gap:12px;margin-top:12px}
.gallery-row .photo{width:105px;height:87px}
.photo.hall{background:radial-gradient(ellipse at 50% 60%,#d9a13f 0%,#7a4d1a 45%,#120d08 80%)}
.photo.station{background:linear-gradient(135deg,#2b5d8c,#7aa6c8 45%,#c0ccd6 60%,#3d4f63)}

.group-band{left:0;top:787px;width:1200px;height:94px;background:var(--band)}
.group-note{left:257px;top:807px;width:190px;font-size:10px;line-height:16px;color:var(--soft)}
.group-link{top:820px;font-size:7.5px;line-height:13px;color:var(--muted)}

.foot-title{top:910px;font-size:10px;color:#fff}
.share-counts{left:257px;top:937px;display:flex;gap:13px}
.count{width:22px;text-align:center}
.count b{display:block;height:13px;background:#fff;color:#333;font-size:6px;line-height:13px;font-weight:400;border-radius:1px}
.count i{display:block;margin-top:5px;height:9px;font-style:normal;font-size:5px;line-height:9px;color:#fff;border-radius:1px}
.share-label{left:364px;top:941px;font-size:7.5px;line-height:9px;color:var(--link)}
.follow{left:257px;top:985px;font-size:7.5px;color:var(--soft);display:flex;align-items:center;gap:5px}
.follow span.dot{width:17px;height:17px;border-radius:50%;background:#5e6873}
.stay{left:257px;top:1010px;font-size:7.5px;color:var(--soft)}
.newsletter{left:257px;top:1022px;width:175px;height:20px;display:flex}
.newsletter .input{flex:1;background:#56606b;font-size:6.8px;color:#dde;padding:6px 5px}
.newsletter .send{width:42px;background:#6f7882;display:flex;align-items:center;justify-content:center}
.news-note{left:257px;top:1047px;width:175px;font-size:6px;line-height:9px;color:var(--muted)}

.other-links{left:465px;top:934px;font-size:7.5px;line-height:13.2px;color:var(--soft);list-style:none}
.foot-divider{left:617px;top:928px;width:1px;height:106px;background:var(--line)}

.reviews{left:644px;top:910px;width:277px}
.reviews .view-all{position:absolute;right:0;top:2px;font-size:7.5px;color:var(--link)}
.review{margin-top:10px;padding-bottom:8px}
.review + .review{border-top:1px solid #8a929b;padding-top:9px;margin-top:0}
.review-head{display:flex;align-items:center;height:12px}
.stars{display:flex;gap:1px}
.review-name{margin-left:10px;font-size:9px;font-style:italic;font-weight:700;color:#8f969e}
.review-meta{margin-left:auto;display:flex;align-items:center;gap:2px;font-size:5.5px;color:var(--muted)}
.review-meta .sq{width:7px;height:7px;background:#5d87b8}
.review-meta .tally{background:#fff;color:#333;padding:0 2px;line-height:8px}
.review p{margin-top:6px;font-size:6.4px;line-height:10px;color:var(--soft)}

.bottom-bar{left:0;top:1070px;width:1200px;height:20px;background:#2a3139;border-top:1px solid #3d4550;text-align:center;font-size:5.5px;line-height:20px;color:var(--muted)}
</style>
</head>
<body>
<div class="canvas">

  <nav class="abs top-nav">
    <a class="current" style="left:236px" href="#">HOME</a>
    <a style="left:294px" href="#">OUR ROOMS</a>
    <a style="left:373px" href="#">ATTRACTIONS</a>
    <a style="left:452px" href="#">LONDON EVENTS</a>
    <a style="left:531px" href="#">SPECIAL OFFERS</a>
    <a style="left:609px" href="#">PHOTOS</a>
    <a style="left:668px" href="#">DIRECTIONS</a>
    <a style="left:746px" href="#">CONTACT</a>
  </nav>

  <header>
    <div class="abs brand-mark"></div>
    <div class="abs brand-name-main" style="left:250px;top:74px;font-size:6px;letter-spacing:.8px;color:var(--muted)">RESTWELL INN · HARBOURLINE HOTELS</div>
    <div class="abs brand-divider"></div>
    <div class="abs brand-location">London - Victoria</div>
    <address class="abs contact" style="font-style:normal">
      42-46 QUAYSIDE ROAD, HARBOURSIDE LONDON HB2 7QL<br>
      STAY@RESTWELLHARBOURSIDE.CO.UK<br>
      TEL: + 44 (0) 20 7946 0183 | FAX:+ 44 (0) 20 7946 0457
    </address>
  </header>

  <div class="abs hero" role="img" aria-label="Photograph of a hotel lounge with patterned armchairs, framed botanical prints and a dark wooden chest of drawers"></div>

  <section class="abs reservation">
    <h2>Reservation</h2>
    <span class="res-label" style="left:228px">Room</span>
    <div class="res-select">Select Room Type<span class="caret"></span></div>
    <span class="res-label" style="left:375px;top:15px">From</span>
    <div class="res-date" style="left:375px">08-11-2013
      <svg width="11" height="11" viewBox="0 0 11 11"><rect x=".5" y="1.5" width="10" height="9" fill="none" stroke="#555"/><rect x=".5" y="1.5" width="10" height="2.5" fill="#555"/><path d="M3 6h1M5 6h1M7 6h1M3 8h1M5 8h1M7 8h1" stroke="#555"/></svg>
    </div>
    <span class="res-label" style="left:469px">To</span>
    <div class="res-date" style="left:469px">10-11-2013
      <svg width="11" height="11" viewBox="0 0 11 11"><rect x=".5" y="1.5" width="10" height="9" fill="none" stroke="#555"/><rect x=".5" y="1.5" width="10" height="2.5" fill="#555"/><path d="M3 6h1M5 6h1M7 6h1M3 8h1M5 8h1M7 8h1" stroke="#555"/></svg>
    </div>
    <a class="res-book" href="#">Book</a>
    <span class="res-sep"></span>
    <a class="res-option" href="#">Option</a>
  </section>

  <section class="abs offers">
    <h2 class="section-title">Latest Offer</h2>
    <div class="offers-list">
      <article class="offer">
        <div class="thumb" role="img" aria-label="Photo of a city station sign against glass buildings"></div>
        <div class="body"><h3>Heading</h3>Lorem ipsum dolor sit amet, consecte-tur adipisicing elit, sed do eiusmod tempor incididunt ut labore et dolore magna aliqua.<br><a class="more" href="#">[ view more ]</a></div>
      </article>
      <article class="offer">
        <div class="thumb" role="img" aria-label="Photo of a city station sign against glass buildings"></div>
        <div class="body"><h3>Heading</h3>Lorem ipsum dolor sit amet, consecte-tur adipisicing elit, sed do eiusmod tempor incididunt ut labore et dolore magna aliqua.<br><a class="more" href="#">[ view more ]</a></div>
      </article>
      <article class="offer">
        <div class="thumb" role="img" aria-label="Photo of a city station sign against glass buildings"></div>
        <div class="body"><h3>Heading</h3>Lorem ipsum dolor sit amet, consecte-tur adipisicing elit, sed do eiusmod tempor incididunt ut labore et dolore magna aliqua.<br><a class="more" href="#">[ view more ]</a></div>
      </article>
    </div>
    <a class="offers-all" href="#">view all offers &gt;&gt;</a>
  </section>

  <section class="abs welcome">
    <h2 class="section-title">Welcome to our Website</h2>
    <p>"Lorem ipsum dolor sit amet, consectetur adipisicing elit, sed do eiusmod tempor incididunt ut labore et dolore magna aliqua. Ut enim ad minim veniam, quis nostrud exercitation ullamco laboris nisi ut aliquip ex ea commodo consequat. Duis aute irure dolor in reprehenderit in voluptate velit esse cillum dolore eu fugiat nulla pariatur. Excepteur sint occaecat cupidatat non proident, sunt in culpa qui officia deserunt mollit anim id est laborum."</p>
    <p>"Lorem ipsum dolor sit amet, consectetur adipisicing elit, sed do eiusmod tempor incididunt ut labore et dolore magna aliqua. Ut enim ad minim veniam, quis nostrud exercitation ullamco laboris nisi ut aliquip ex ea commodo consequat. Duis aute irure dolor in reprehenderit in voluptate velit esse cillum dolore eu fugiat nulla pariatur. Excepteur sint occaecat cupidatat non proident, sunt in culpa qui officia deserunt mollit anim id est laborum."</p>
  </section>

  <section class="abs gallery">
    <h2 class="section-title">Gallery</h2>
    <a class="view-all" href="#">view all &gt;&gt;</a>
    <div class="gallery-row">
      <div class="photo hall" role="img" aria-label="Photo of a domed concert hall lit at night"></div>
      <div class="photo station" role="img" aria-label="Photo of a city station sign against glass buildings"></div>
      <div class="photo hall" role="img" aria-label="Photo of a domed concert hall lit at night"></div>
      <div class="photo station" role="img" aria-label="Photo of a city station sign against glass buildings"></div>
    </div>
  </section>

  <section class="abs group-band"></section>
  <p class="abs group-note">This hotel is owned and operated by the Northgate Hotel Group, please take a look of some of our other hotels</p>
  <a class="abs group-link" style="left:465px" href="#">Maple Lodge London<br>- Camden Lock</a>
  <a class="abs group-link" style="left:557px" href="#">Maple Lodge Express<br>- Earls Court</a>
  <a class="abs group-link" style="left:651px" href="#">Centre Point<br>Rooms</a>
  <a class="abs group-link" style="left:723px" href="#">SimpleStay<br>Victoria</a>
  <a class="abs group-link" style="left:788px" href="#">SimpleStay<br>Paddington</a>
  <a class="abs group-link" style="left:856px" href="#">Restwell Suites<br>- King's Cross</a>

  <footer>
    <h3 class="abs foot-title" style="left:257px;font-weight:400">Share Your Holiday with Friends</h3>
    <div class="abs share-counts">
      <div class="count"><b>868</b><i style="background:#3aa3d9">Post</i></div>
      <div class="count"><b>1.3K</b><i style="background:#4e69a2">Like</i></div>
      <div class="count"><b>28</b><i style="background:#555">+1</i></div>
    </div>
    <a class="abs share-label" href="#">SHARE<br>London Victoria</a>
    <div class="abs follow">Follow Us <span class="dot"></span><span class="dot"></span><span class="dot"></span><span class="dot"></span></div>
    <div class="abs stay">Stay in Touch</div>
    <div class="abs newsletter">
      <div class="input">email@email.com</div>
      <div class="send"><svg width="14" height="10" viewBox="0 0 14 10"><rect x=".5" y=".5" width="13" height="9" fill="none" stroke="#fff"/><path d="M.5 .5 7 6 13.5 .5" fill="none" stroke="#fff"/></svg></div>
    </div>
    <p class="abs news-note">Sign up for our newsletter for latest news from Restwell Inn London - Victoria</p>

    <h3 class="abs foot-title" style="left:465px;font-weight:400">Other Links</h3>
    <ul class="abs other-links">
      <li>Maple Lodge London - Camden Lock</li>
      <li>Maple Lodge Express - Earls Court</li>
      <li>Centre Point Rooms</li>
      <li>SimpleStay Victoria</li>
      <li>SimpleStay Paddington</li>
      <li>Restwell Suites - King's Cross</li>
    </ul>
    <div class="abs foot-divider"></div>

    <section class="abs reviews">
      <h3 class="foot-title" style="position:static;font-weight:400">Journeyrater Review</h3>
      <a class="view-all" href="#">view all &gt;&gt;</a>
      <article class="review">
        <div class="review-head">
          <div class="stars">
            <svg width="52" height="10" viewBox="0 0 52 10"><g id="s"><path d="M5 0l1.5 3.2 3.5.4-2.6 2.4.7 3.5L5 7.8 1.9 9.5l.7-3.5L0 3.6l3.5-.4z"/></g>
              <use href="#s" fill="var(--star)"/><use href="#s" x="10.5" fill="var(--star)"/><use href="#s" x="21" fill="var(--star)"/><use href="#s" x="31.5" fill="var(--star-off)"/><use href="#s" x="42" fill="var(--star-off)"/></svg>
          </div>
          <span class="review-name">Abcdefg Hijklm</span>
          <span class="review-meta">2hr ago&nbsp; <span class="sq"></span><span class="sq"></span><span class="sq"></span><span class="sq"></span><span class="sq"></span><span class="tally">1.4M</span></span>
        </div>
        <p>Lorem ipsum dolor sit amet, consectetur adipisicing elit, sed do eiusmod tempor incididunt ut labore et dolore magna aliqua. Ut enim ad minim veniam</p>
      </article>
      <article class="review">
        <div class="review-head">
          <div class="stars">
            <svg width="52" height="10" viewBox="0 0 52 10">
              <use href="#s" fill="var(--star)"/><use href="#s" x="10.5" fill="var(--star)"/><use href="#s" x="21" fill="var(--star-off)"/><use href="#s" x="31.5" fill="var(--star-off)"/><use href="#s" x="42" fill="var(--star-off)"/></svg>
          </div>
          <span class="review-name">Abcdefg Hijklm</span>
          <span class="review-meta">2hr ago&nbsp; <span class="sq"></span><span class="sq"></span><span class="sq"></span><span class="sq"></span><span class="sq"></span><span class="tally">1.4M</span></span>
        </div>
        <p>Lorem ipsum dolor sit amet, consectetur adipisicing elit, sed do eiusmod tempor incididunt ut labore et dolore magna aliqua. Ut enim ad minim veniam</p>
      </article>
    </section>

    <div class="abs bottom-bar">All Right Reserved 2013 London Victoria.</div>
  </footer>

</div>
</body>
</html>
```